Need Flyer for Our Real estate Agency

Need to run General Campaign for our agency with Start of New Year as our theme ..Must have an agent's picture on the DL..
Address:
27 / 348Marlow rd, Harlowe Park VIC 3041
Ph:03 9412 7305
email:info@koralinrealestate.com.au
www.koralinrealestate.com.au
Something like as attached picture..
Target Market(s)
Home Buyers
Industry/Entity Type
Real Estate Agent
Requirements
Must have
- Our Logo Colours

```html
<!DOCTYPE html>
<html lang="en">
<head>
<meta charset="utf-8">
<title>Koralin Real Estate – Appraisal Flyer</title>
<link rel="stylesheet" href="https://fonts.googleapis.com/css2?family=EB+Garamond:wght@500;600;700&family=Roboto:wght@300&display=swap">
<style>
  :root {
    --navy-deep: #1d1f52;
    --navy-mid: #26306e;
    --blue-glow: #3b57a6;
    --white: #ffffff;
    --accent-red: #7a1622;
    --photo-blue: #3d5e9c;
    --photo-skin: #8a6a5a;
  }
  * { margin: 0; padding: 0; box-sizing: border-box; }
  html, body { width: 1200px; height: 566px; overflow: hidden; background: var(--navy-deep); }
  .flyer {
    position: relative;
    width: 1200px;
    height: 566px;
    overflow: hidden;
    background:
      radial-gradient(ellipse 520px 300px at 830px 170px, var(--blue-glow) 0%, rgba(59,87,166,0.55) 45%, rgba(38,48,110,0) 100%),
      linear-gradient(160deg, var(--navy-mid) 0%, var(--navy-deep) 70%);
  }
  .hero-curve { position: absolute; left: 0; top: 0; }
  .agent-photo {
    position: absolute;
    left: 104px;
    top: 12px;
    width: 296px;
    height: 404px;
    border-radius: 140px 140px 0 0;
    background: linear-gradient(180deg, var(--photo-skin) 0%, var(--photo-skin) 38%, var(--photo-blue) 42%, #2e4a82 100%);
  }
  .headline {
    position: absolute;
    left: 380px;
    top: 140px;
    width: 730px;
    text-align: center;
    font-family: "EB Garamond", serif;
    font-weight: 600;
    font-size: 49px;
    line-height: 49px;
    letter-spacing: 1px;
    color: var(--white);
    text-transform: uppercase;
  }
  .intro {
    position: absolute;
    left: 420px;
    top: 258px;
    width: 650px;
    text-align: center;
    font-family: "Roboto", sans-serif;
    font-weight: 300;
    font-size: 14.5px;
    line-height: 19px;
    color: var(--white);
  }
  .footer-band {
    position: absolute;
    left: 0; top: 416px;
    width: 1200px; height: 150px;
    background: var(--navy-deep);
  }
  .brand-name {
    position: absolute;
    left: 44px;
    top: 488px;
    width: 280px;
    text-align: center;
    white-space: nowrap;
    font-family: "EB Garamond", serif;
    font-weight: 500;
    font-size: 21px;
    letter-spacing: 2px;
    color: var(--white);
  }
  .call {
    position: absolute;
    left: 390px;
    top: 458px;
    font-family: "EB Garamond", serif;
  }
  .call-label { font-size: 21px; font-weight: 700; color: var(--accent-red); line-height: 22px; }
  .call-number { font-size: 39px; font-weight: 700; color: var(--white); line-height: 44px; letter-spacing: 1px; }
  .contact-list {
    position: absolute;
    left: 736px;
    top: 457px;
    list-style: none;
    white-space: nowrap;
    font-family: "EB Garamond", serif;
    font-size: 15px;
    font-weight: 700;
    line-height: 24.5px;
    color: var(--white);
  }
  .contact-label { color: var(--accent-red); font-weight: 600; }
</style>
</head>
<body>
<main class="flyer">
  <svg class="hero-curve" width="1200" height="416" viewBox="0 0 1200 416" aria-hidden="true">
    <path d="M0,190 Q90,400 420,416 L0,416 Z" fill="#1d1f52"/>
  </svg>

  <div class="agent-photo" role="img" aria-label="Portrait photo of a smiling agent in a blue checked suit and striped tie"></div>

  <h1 class="headline">Curious to know what<br>your home worth?</h1>
  <p class="intro">Lorem ipsum dolor sit amet, consectetuer adipiscing elit, sed diam nonummy nibh<br>euismod tincidunt ut laoreet dolore magna aliquam erat volutpat. Ut wisi enim ad minim</p>

  <footer class="footer-band"></footer>

  <div class="brand-name">KORALIN REAL ESTATE</div>

  <div class="call">
    <div class="call-label">Call Now:</div>
    <div class="call-number">03 9412 7305</div>
  </div>

  <ul class="contact-list">
    <li><span class="contact-label">Address:</span> 27 / 348Marlow rd, Harlowe Park VIC 3041</li>
    <li><span class="contact-label">Email:</span> info@koralinrealestate.com.au</li>
    <li><span class="contact-label">Website:</span> www.koralinrealestate.com.au</li>
  </ul>
</main>
</body>
</html>
```